Business Card Design Project

I need a business card for an environmentally friendly interior design company called Roomcraft Willow.
I was thinking it might be nice to print the business cards on brown recycled paper with green ink.
In addition to interior design, I will also be able to consult with homeowners regarding their indoor environments and how they might be affecting their health after May 2013 which is when I will complete my certification program. This can be added to the business card at that time: "Certified Habitat Vitalis Dwelling Consultant".
Health

```html
<!DOCTYPE html>
<html lang="en">
<head>
<meta charset="utf-8">
<title>Roomcraft Willow — Business Cards</title>
<link rel="stylesheet" href="https://fonts.googleapis.com/css2?family=Nunito:wght@300;400;800&family=Arimo:wght@400&display=swap">
<style>
  :root {
    --backdrop: #ece8e1;
    --kraft: #c9b99b;
    --kraft-shade: #b9a888;
    --ink-green: #13924a;
  }
  html, body {
    margin: 0;
    padding: 0;
    width: 1200px;
    height: 880px;
    overflow: hidden;
    background: var(--backdrop);
  }
  .canvas {
    position: relative;
    width: 1200px;
    height: 880px;
  }
  .card {
    position: absolute;
    width: 525px;
    height: 300px;
    background: var(--kraft);
    overflow: hidden;
    box-shadow: 0 6px 18px rgba(60, 45, 25, 0.18);
    color: var(--ink-green);
  }

  /* Front side */
  .card-front {
    left: 70px;
    top: 420px;
    display: flex;
    flex-direction: column;
    align-items: center;
    justify-content: center;
  }
  .brand-mark {
    width: 84px;
    height: 84px;
    border-radius: 50%;
    background: var(--ink-green);
    margin-bottom: 18px;
  }
  .brand-name {
    font-family: "Nunito", sans-serif;
    font-weight: 800;
    font-size: 42px;
    line-height: 1;
    margin: 0;
    letter-spacing: 0.3px;
  }
  .brand-tagline {
    font-family: "Nunito", sans-serif;
    font-weight: 400;
    font-size: 19px;
    margin: 6px 0 0;
    letter-spacing: 0.4px;
  }

  /* Back side */
  .card-back {
    left: 605px;
    top: 150px;
  }
  .corner-disc {
    position: absolute;
    left: -90px;
    top: -90px;
    width: 230px;
    height: 230px;
    border-radius: 50%;
    background: var(--ink-green);
  }
  .back-brand {
    position: absolute;
    right: 30px;
    top: 34px;
    text-align: right;
  }
  .back-brand .brand-name {
    font-size: 34px;
  }
  .credential {
    font-family: "Arimo", sans-serif;
    font-size: 11.5px;
    margin: 6px 0 0;
  }
  .contact {
    position: absolute;
    left: 150px;
    right: 30px;
    top: 150px;
  }
  .person-name {
    font-family: "Nunito", sans-serif;
    font-weight: 800;
    font-size: 44px;
    line-height: 1;
    margin: 0;
  }
  .phone {
    font-family: "Nunito", sans-serif;
    font-weight: 300;
    font-size: 36px;
    line-height: 1;
    margin: 14px 0 0;
    letter-spacing: 1px;
  }
</style>
</head>
<body>
<main class="canvas">
  <section class="card card-front">
    <div class="brand-mark" aria-hidden="true"></div>
    <h1 class="brand-name">Roomcraft Willow</h1>
    <p class="brand-tagline">Environmentally Friendly Design</p>
  </section>

  <section class="card card-back">
    <div class="corner-disc" aria-hidden="true"></div>
    <div class="back-brand">
      <h2 class="brand-name">Roomcraft Willow</h2>
      <p class="credential">Certified Habitat Vitalis Dwelling Consultant</p>
    </div>
    <div class="contact">
      <p class="person-name">Della Rae Corbin</p>
      <p class="phone">555-214-7730</p>
    </div>
  </section>
</main>
</body>
</html>
```